KVRo Business Cards

We need a business card design. We are a Technology (Audio Visual) design, sales and installation company. Looking for a double sided design, clean

Contact Information for Business Card

Clean, modern look, 2 sided

Font styles to use
Sans Serif

```html
<!DOCTYPE html>
<html lang="en">
<head>
<meta charset="UTF-8">
<title>KVRo Business Cards</title>
<link rel="stylesheet" href="https://fonts.googleapis.com/css2?family=Montserrat:wght@400;600;700;800&display=swap">
<style>
  :root {
    --navy: #1b2d3d;
    --orange: #f0941f;
    --white: #ffffff;
    --paper: #fbfbfb;
    --grey-text: #55595e;
    --backdrop: #e6e7e9;
  }
  * { margin: 0; padding: 0; box-sizing: border-box; }
  html, body {
    width: 1200px;
    height: 900px;
    overflow: hidden;
    background: var(--backdrop);
    font-family: "Montserrat", sans-serif;
  }
  .sheet {
    position: relative;
    width: 1200px;
    height: 900px;
  }
  .card {
    position: absolute;
    left: 250px;
    width: 700px;
    height: 400px;
    border-radius: 4px;
    box-shadow: 0 6px 18px rgba(0,0,0,0.15);
    overflow: hidden;
  }
  .card--front { top: 40px; background: var(--paper); }
  .card--back  { top: 460px; background: var(--navy); display: flex; align-items: center; justify-content: center; }

  .brand-name {
    font-weight: 800;
    letter-spacing: -2px;
    line-height: 1;
  }
  .card--front .brand-name {
    position: absolute;
    left: 60px;
    top: 140px;
    font-size: 112px;
    color: var(--navy);
  }
  .card--back .brand-name {
    font-size: 190px;
    color: var(--white);
  }

  .divider {
    position: absolute;
    left: 372px;
    top: 100px;
    width: 3px;
    height: 200px;
    background: var(--navy);
  }
  .divider::after {
    content: "";
    position: absolute;
    left: 0;
    top: 45px;
    width: 3px;
    height: 110px;
    background: var(--orange);
  }

  .details {
    position: absolute;
    left: 400px;
    top: 112px;
    color: var(--navy);
  }
  .person-name {
    font-size: 30px;
    font-weight: 800;
    letter-spacing: 1px;
    text-transform: uppercase;
  }
  .person-name .surname { color: var(--orange); }
  .person-title {
    font-size: 21px;
    font-weight: 400;
    color: var(--grey-text);
    margin-top: 2px;
  }
  .contact-list {
    list-style: none;
    margin-top: 16px;
  }
  .contact-item {
    display: flex;
    align-items: center;
    gap: 10px;
    font-size: 22px;
    color: var(--grey-text);
    line-height: 1.55;
  }
  .contact-item svg { width: 18px; height: 18px; flex: none; }
  .accent { color: var(--orange); }
</style>
</head>
<body>
<main class="sheet">
  <section class="card card--front" aria-label="Business card front">
    <div class="brand-name">KVRo</div>
    <div class="divider"></div>
    <div class="details">
      <h1 class="person-name">Marcus <span class="surname">Hale</span></h1>
      <p class="person-title">Founder &amp; CEO</p>
      <ul class="contact-list">
        <li class="contact-item">
          <svg viewBox="0 0 24 24" aria-hidden="true"><path fill="#f0941f" d="M6.6 10.8a15.1 15.1 0 0 0 6.6 6.6l2.2-2.2c.3-.3.7-.4 1-.2 1.1.4 2.3.6 3.6.6.6 0 1 .4 1 1V20c0 .6-.4 1-1 1A17 17 0 0 1 3 4c0-.6.4-1 1-1h3.5c.6 0 1 .4 1 1 0 1.3.2 2.5.6 3.6.1.3 0 .7-.2 1z"/></svg>
          555-014-2739
        </li>
        <li class="contact-item">
          <svg viewBox="0 0 24 24" aria-hidden="true"><path fill="#f0941f" d="M2 5h20v14H2z"/><path fill="none" stroke="#fbfbfb" stroke-width="1.6" d="M2 5l10 8 10-8"/></svg>
          marcus.h@kvro.com
        </li>
        <li class="contact-item">
          <svg viewBox="0 0 24 24" aria-hidden="true"><circle cx="12" cy="12" r="10" fill="#f0941f"/><path fill="none" stroke="#fbfbfb" stroke-width="1.4" d="M2 12h20M12 2c3 3 3 17 0 20M12 2c-3 3-3 17 0 20"/></svg>
          <span>www.<span class="accent">kvro</span>.com</span>
        </li>
      </ul>
    </div>
  </section>

  <section class="card card--back" aria-label="Business card back">
    <div class="brand-name">KVRo</div>
  </section>
</main>
</body>
</html>
```